Instructions for nurses on how to give a report on each shift

I have a 2-page reference sheet that needs to be updated to look more aesthetically pleasing.

Target Market(s)

Healthcare, nurses

Industry/Entity Type

Healthcare

Font styles to use
Sans Serif

Requirements
Must have
• Please make sure it is easy to read, the content is well organized and has a flow to it. Please also pick colors that would coordinate with our website www.ovtrime.org (so mainly navy and white or off-white with accent colors.) Please make sure to add accent colors to break up the content. The BORSK name and title at the top should remain on the page but I'm not married to the star or logo style. You can do what you think looks best there. Way at the bottom in fine print, I would like for you to add OVTRIME © 2019 All rights reserved.

```html
<!DOCTYPE html>
<html lang="en">
<head>
<meta charset="utf-8">
<title>BORSK Shift Report Reference Sheet</title>
<link href="https://fonts.googleapis.com/css2?family=Montserrat:wght@600;700;800;900&family=Lato:wght@400;700&display=swap" rel="stylesheet">
<style>
:root{
  --navy:#0f3a63;
  --navy-deep:#0b2d4f;
  --ink:#111417;
  --black:#15171a;
  --paper:#ffffff;
  --paper-soft:#eeeeee;
  --rule:#9a9a9a;
  --backdrop:#8e8e8e;
}
*{box-sizing:border-box;margin:0;padding:0}
html,body{width:1200px;height:1200px;overflow:hidden;background:var(--backdrop)}
body{position:relative;font-family:"Lato",sans-serif;color:var(--ink)}
.page{position:absolute;top:222px;width:539px;height:696px;background:linear-gradient(180deg,var(--paper) 0%,var(--paper-soft) 100%);overflow:hidden}
.page--guide{left:44px}
.page--form{left:630px}
.abs{position:absolute}

/* guide page */
.brand-title{position:absolute;left:20px;top:8px;font-family:"Montserrat",sans-serif;font-weight:900;font-size:50px;letter-spacing:1px;color:var(--navy);line-height:1}
.hero{position:absolute;left:0;top:66px;width:539px;height:232px}
.hero-photo{position:absolute;left:0;top:0;width:539px;height:232px;background:linear-gradient(120deg,#d9d3ca 0%,#c4b7a8 35%,#6b7fb0 55%,#cfc6bc 80%)}
.hero-shapes{position:absolute;left:0;top:-66px}
.tagline{position:absolute;left:332px;top:75px;color:#fff;font-family:"Montserrat",sans-serif;line-height:1.25}
.tagline .lead{font-size:12px;font-weight:600}
.tagline .strong{font-size:15px;font-weight:900;letter-spacing:.3px}
.tagline .strong.indent{padding-left:7px}
.section{position:absolute}
.section h2{font-family:"Montserrat",sans-serif;font-weight:800;font-size:12.5px;color:var(--navy);letter-spacing:.3px;margin-bottom:3px}
.checklist{list-style:none}
.checklist li{position:relative;padding-left:17px;font-size:9px;line-height:14px}
.checklist li.wrap{line-height:12px;margin:1px 0 2px}
.checklist li::before{content:"";position:absolute;left:4px;top:3px;width:3px;height:6px;border:solid var(--navy);border-width:0 2px 2px 0;transform:rotate(40deg)}
.checklist li.wrap::before{top:2px}
.divider{position:absolute;left:18px;width:502px;height:1px;background:var(--rule)}
.col-rule{position:absolute;left:254px;width:1px;background:#c8c8c8}
.footer{position:absolute;left:0;bottom:0;width:100%;height:24px;background:var(--navy);color:#fff;font-size:11px;text-align:center;line-height:24px}

/* form page */
.top-bar{position:absolute;left:0;top:0;width:100%;height:8px;background:var(--black)}
.header-box{position:absolute;left:18px;top:19px;width:501px;height:73px;border:2px solid var(--ink);background:#fff}
.header-box .brand-title{left:12px;top:12px;font-size:22px;letter-spacing:.5px}
.fields{position:absolute;left:122px;top:12px;font-size:11px;line-height:16px}
.question{position:absolute;left:18px;width:221px;border:2px solid var(--ink);background:#fff;padding:5px 0 0 14px}
.question h3{font-family:"Montserrat",sans-serif;font-weight:800;font-size:11.5px;line-height:16px;margin-bottom:1px}
.topics{display:grid;grid-template-columns:105px 1fr;padding-left:15px;font-size:11.5px;line-height:16px}
.topics.single{grid-template-columns:1fr}
.answer{position:absolute;left:265px;width:254px;border:2px solid var(--ink);background:#fff;padding:5px 8px 0 9px;font-size:7.4px;line-height:10px}
.answer .label{font-size:8px}
.blanks{display:flex;gap:0;margin-top:4px}
.blanks span{width:76px}
.blanks span i{display:inline-block;width:50px;border-bottom:1px solid var(--ink);margin-left:1px}
.connectors{position:absolute;left:0;top:0}
.page--form .footer{bottom:6px}
.bottom-bar{position:absolute;left:0;bottom:0;width:100%;height:6px;background:var(--black)}
</style>
</head>
<body>

<section class="page page--guide">
  <div class="brand-title">BORSK</div>
  <div class="hero">
    <div class="hero-photo" role="img" aria-label="Photo of two clinicians caring for a smiling older patient sitting up in a hospital bed"></div>
    <svg class="hero-shapes" width="539" height="298" viewBox="0 0 539 298">
      <polygon points="368,0 539,0 539,66 408,66" fill="var(--navy)"/>
      <polygon points="408,66 539,66 539,0" fill="var(--black)" opacity=".95"/>
      <polygon points="408,66 539,66 539,0 470,40" fill="var(--black)"/>
      <polygon points="288,66 539,66 539,298 300,298 318,180" fill="var(--navy-deep)"/>
      <polygon points="539,180 539,298 360,298" fill="var(--black)"/>
    </svg>
    <div class="tagline">
      <div class="lead">When “I” is replaced by “WE”</div>
      <div class="strong">EVEN ILLNESS</div>
      <div class="strong indent">BECOMES WELLNESS.</div>
    </div>
  </div>

  <div class="section" style="left:20px;top:314px">
    <h2>OBJECTIVES:</h2>
    <ul class="checklist">
      <li>Accountability: Declare roles and assignments</li>
      <li>Advocacy: Identify patient needs</li>
      <li>Critical Thinking: Prioritize and recognize obstacles</li>
      <li>Communication: Share important information</li>
      <li>Collaboration: Utilize an interdisciplinary approach</li>
    </ul>
  </div>
  <div class="section" style="left:262px;top:314px;width:270px">
    <h2>WHO:</h2>
    <ul class="checklist">
      <li>All nurses on the unit</li>
      <li>All nursing support staff (CNA/MA/HCT)</li>
      <li>Administrator</li>
      <li>Director of Nursing</li>
      <li>Head of pertinent disciplines (Dietary, Social Work, Physical Therapy, Engineering, Central Supply, etc.)</li>
    </ul>
  </div>
  <div class="col-rule" style="top:318px;height:100px"></div>
  <div class="divider" style="top:425px"></div>

  <div class="section" style="left:20px;top:438px">
    <h2>OUTCOMES:</h2>
    <ul class="checklist">
      <li>Share best practices</li>
      <li>Improve communication</li>
      <li>Promote cohesiveness</li>
      <li>Increase staff morale</li>
      <li>Enhance patient and organizational outcomes</li>
    </ul>
  </div>
  <div class="section" style="left:262px;top:438px">
    <h2>WHEN:</h2>
    <ul class="checklist">
      <li>Every morning (assign a meeting time for each unit)</li>
      <li>Keep meetings within 15 minutes in length</li>
    </ul>
    <h2 style="margin-top:6px">WHERE</h2>
    <ul class="checklist">
      <li>Nursing station on each unit</li>
    </ul>
  </div>
  <div class="col-rule" style="top:436px;height:94px"></div>
  <div class="divider" style="top:535px"></div>

  <div class="section" style="left:20px;top:548px;width:250px">
    <h2>HELPFUL TIPS:</h2>
    <ul class="checklist">
      <li class="wrap">Assign a meeting facilitator (usually the administrator of the facility)</li>
      <li class="wrap">Standing during meetings keeps the meetings short and to the point</li>
      <li class="wrap">Keeping meetings within 15 minutes emphasizes being prepared and direct</li>
      <li class="wrap">Keep meeting times consistent (morning is best)</li>
    </ul>
  </div>
  <div class="section" style="left:262px;top:566px;width:250px">
    <ul class="checklist">
      <li class="wrap">Do not begin until everyone is present (minimizes stragglers)</li>
      <li class="wrap">Avoid discussing personal concerns</li>
      <li class="wrap">Include reminders for in-services, meetings, etc. and updates towards the end of the meeting</li>
      <li class="wrap">Always conclude with achievements, milestones, praise, words of encouragement, motivational quote, etc.</li>
    </ul>
  </div>

  <div class="footer">OVTRIME © 2019 All rights reserved</div>
</section>

<section class="page page--form">
  <div class="top-bar"></div>
  <div class="header-box">
    <div class="brand-title">BORSK</div>
    <div class="fields">Name:<br>Title:<br>Assignment:</div>
  </div>

  <svg class="connectors" width="539" height="696" viewBox="0 0 539 696">
    <g stroke="var(--ink)" stroke-width="1.5" fill="none">
      <line x1="94" y1="92" x2="94" y2="535"/>
      <polyline points="239,133 246,133 246,182"/>
      <polyline points="246,133 246,133"/>
      <polyline points="239,259 246,259 246,288"/>
      <polyline points="239,352 246,352 246,400"/>
      <polyline points="239,460 246,460 246,508"/>
      <polyline points="239,572 246,572 246,627"/>
      <line x1="246" y1="133" x2="246" y2="182"/>
      <line x1="246" y1="239" x2="246" y2="288"/>
      <line x1="246" y1="352" x2="246" y2="400"/>
      <line x1="246" y1="460" x2="246" y2="508"/>
      <line x1="246" y1="572" x2="246" y2="627"/>
    </g>
    <g fill="var(--navy)">
      <path d="M250 131h6v-4l7 6-7 6v-4h-6z"/>
      <path d="M250 180h6v-4l7 6-7 6v-4h-6z"/>
      <path d="M250 237h6v-4l7 6-7 6v-4h-6z"/>
      <path d="M250 286h6v-4l7 6-7 6v-4h-6z"/>
      <path d="M250 350h6v-4l7 6-7 6v-4h-6z"/>
      <path d="M250 398h6v-4l7 6-7 6v-4h-6z"/>
      <path d="M250 458h6v-4l7 6-7 6v-4h-6z"/>
      <path d="M250 506h6v-4l7 6-7 6v-4h-6z"/>
      <path d="M250 570h6v-4l7 6-7 6v-4h-6z"/>
      <path d="M250 625h6v-4l7 6-7 6v-4h-6z"/>
    </g>
  </svg>

  <div class="question" style="top:107px;height:91px">
    <h3>Any change in resident status?</h3>
    <div class="topics single"><span>Admissions</span><span>Discharges</span><span>Transfers</span><span>Appointments</span></div>
  </div>
  <div class="answer" style="top:107px;height:53px">
    <div class="label">YES</div>“My residents with changes in their status are…”
    <div class="blanks"><span>1)<i></i></span><span>2)<i></i></span><span>3)<i></i></span></div>
  </div>
  <div class="answer" style="top:166px;height:32px">
    <div class="label">NO</div>“I do not have any actual or expected changes in resident status.”
  </div>

  <div class="question" style="top:206px;height:106px">
    <h3>Any concerning changes in resident’s condition?</h3>
    <div class="topics"><span>Pain</span><span>Skin</span><span>Ambulation</span><span>Safety</span><span>Behavior</span><span></span><span>Appetite</span><span>Elimination</span></div>
  </div>
  <div class="answer" style="top:213px;height:52px">
    <div class="label">YES</div>“My residents w/ concerning changes in their condition include…”
    <div class="blanks"><span>1)<i></i></span><span>2)<i></i></span><span>3)<i></i></span></div>
  </div>
  <div class="answer" style="top:272px;height:32px">
    <div class="label">NO</div>“I have no residents with concerning changes in their condition.”
  </div>

  <div class="question" style="top:319px;height:104px">
    <h3>Any residents requiring extraordinary monitoring?</h3>
    <div class="topics single"><span>Falls</span><span>Decline in condition</span><span>IV/ABT therapy</span><span>Hospice</span></div>
  </div>
  <div class="answer" style="top:326px;height:52px">
    <div class="label">YES</div>“My residents that require extraordinary monitoring are…”
    <div class="blanks"><span>1)<i></i></span><span>2)<i></i></span><span>3)<i></i></span></div>
  </div>
  <div class="answer" style="top:384px;height:32px">
    <div class="label">NO</div>“I have no residents requiring extraordinary monitoring.”
  </div>

  <div class="question" style="top:433px;height:92px">
    <h3>Any concerns related to residents environment?</h3>
    <div class="topics single"><span>Room temperature</span><span>Supplies</span><span>Equipment</span></div>
  </div>
  <div class="answer" style="top:434px;height:52px">
    <div class="label">YES</div>“My residents with concerns related to their environment include…”
    <div class="blanks"><span>1)<i></i></span><span>2)<i></i></span><span>3)<i></i></span></div>
  </div>
  <div class="answer" style="top:491px;height:33px">
    <div class="label">NO</div>“I have no concerns related to my residents environment.”
  </div>

  <div class="question" style="top:535px;height:124px">
    <h3>Any concerns or barriers related to your ability to perform your job effectively?</h3>
    <div class="topics"><span>Supplies</span><span>Acuity</span><span>Time constraints</span><span></span><span>Family requests</span><span></span><span>Environment</span></div>
  </div>
  <div class="answer" style="top:546px;height:52px">
    <div class="label">YES</div>“My concerns affecting my ability to perform my job include…”
    <div class="blanks"><span>1)<i></i></span><span>2)<i></i></span><span>3)<i></i></span></div>
  </div>
  <div class="answer" style="top:605px;height:43px">
    <div class="label">NO</div>“I have no concerns or barriers affecting my ability to perform my job.”
  </div>

  <div class="footer">OVTRIME © 2019 All rights reserved</div>
  <div class="bottom-bar"></div>
</section>

</body>
</html>
```